Brightfield Co Trade Show Flyer

We need a brochure design (8.5 x 11) Info in the design (refer to rough draft I drew on Paper): "#1 selling tool to aquire new franchisees has been video testimonials" - Martin L. Crowe, C.E.O Tovik Smoothie Franchise Testimonials - Let your franchisees do the selling for you. Franchisee testimonial: $10,000 / per Franchisee Includes: • 2 minute Video • 1 minute add for your franchise's location • Concept creation • Communication with franchisee • Travel to their location • All rental equipment • 1 round of corrections • Animated logo • Licensed music ******* For 25% Discount section (next to middle box), please put the "Outlet Summit Logo" Great to use on all your social media (USE logos and icons) • Website • YouTube • LinkedIn • Facebook • Instagram • Twitter • Phone calls • Emails • In person meetings Some of our clients: (use the logos I uploaded - in round boxes as in draft) LOGO (Brightfield Franchise Testimonial) www.brightfieldvoices.example (866) 555-0172

Target Market(s)

Franchise owners

Colors

Designer to choose colors to be used in the design.

Requirements

```html
<!DOCTYPE html>
<html lang="en">
<head>
<meta charset="utf-8">
<title>Brightfield Franchise Testimonials Flyer</title>
<link href="https://fonts.googleapis.com/css2?family=Kurale&family=Open+Sans:wght@300;400;600;700&display=swap" rel="stylesheet">
<style>
  :root{
    --page:#e9e9e9;
    --band:#a0111d;
    --red:#d31a26;
    --red-dark:#8e0e18;
    --ink:#0c0b10;
    --panel:#232323;
    --white:#ffffff;
    --tick:#d31a26;
    --teal:#26a89a;
  }
  *{box-sizing:border-box;margin:0;padding:0}
  html,body{width:1200px;height:1200px;overflow:hidden;background:var(--page)}
  .flyer{position:absolute;left:181px;top:59px;width:838px;height:1082px;background:var(--ink);overflow:hidden;font-family:"Open Sans",sans-serif;color:var(--white);box-shadow:0 20px 40px rgba(0,0,0,.25)}
  .top-band{position:absolute;left:0;top:0;width:100%;height:99px;background:var(--band)}
  .quote-frame{position:absolute;left:62px;top:16px;width:716px;height:57px;border:1.5px solid var(--white)}
  .quote{position:absolute;left:0;top:13px;width:100%;text-align:center;font-family:"Kurale",serif;font-size:23px;letter-spacing:1px;white-space:nowrap}
  .quote b{font-family:"Open Sans",sans-serif;font-weight:700;font-size:25px}
  .quote-credit{position:absolute;left:50%;top:63px;transform:translateX(-50%);padding:0 14px;background:var(--band);font-weight:700;font-size:14px;letter-spacing:3px;white-space:nowrap}
  .dark-field{position:absolute;left:0;top:99px;width:100%;height:839px;background:radial-gradient(ellipse at 85% 70%,rgba(160,20,30,.55),transparent 55%),radial-gradient(ellipse at 10% 60%,rgba(140,15,25,.45),transparent 50%),var(--ink)}
  .title-badge{position:absolute;left:183px;top:137px;width:471px;height:113px;border-radius:8px;background:linear-gradient(180deg,#e4222d,#a8111c);box-shadow:0 4px 10px rgba(0,0,0,.5)}
  .title-badge span{position:absolute;left:0;top:0;width:100%;line-height:113px;text-align:center;font-weight:600;font-size:68px}
  .title-main{position:absolute;left:0;top:258px;width:100%;text-align:center;font-weight:600;font-size:88px;line-height:100px;letter-spacing:-1px}
  .tagline{position:absolute;left:0;top:366px;width:100%;text-align:center;color:var(--red);font-size:19px;letter-spacing:3px}
  .price-panel{position:absolute;left:74px;top:423px;width:690px;height:282px;background:var(--panel)}
  .price{position:absolute;left:25px;top:14px;font-family:"Kurale",serif;font-size:46px;line-height:46px;white-space:nowrap}
  .price small{font-size:23px;margin-left:8px}
  .includes{position:absolute;left:25px;top:72px;list-style:none;font-family:"Kurale",serif;font-size:18px}
  .includes li{display:block;height:22px;line-height:22px;white-space:nowrap;overflow:hidden}
  .includes li::before{content:"\221A";color:var(--tick);font-size:13px;line-height:1;margin-right:6px}
  .discount{position:absolute;left:560px;top:515px;width:218px;height:218px;border-radius:50%;background:radial-gradient(circle at 40% 30%,#e6323c,#a80f1b 75%);border:4px solid #f3d6d8;box-shadow:0 6px 14px rgba(0,0,0,.5);text-align:center;font-weight:700}
  .discount .pct{display:block;margin-top:40px;font-size:70px;line-height:70px}
  .discount .label{display:block;font-size:28px;line-height:36px}
  .tag{position:absolute;left:622px;top:780px;width:150px;height:92px;transform:rotate(-32deg);background:var(--white);border-radius:10px 40px 40px 10px;box-shadow:0 4px 8px rgba(0,0,0,.4)}
  .tag .badge{position:absolute;left:10px;top:14px;width:100px;height:64px;background:var(--teal)}
  .tag-string{position:absolute;left:0;top:0}
  .section-label{position:absolute;left:74px;font-family:"Kurale",serif;color:var(--red-dark);font-size:17px;letter-spacing:1px;text-transform:uppercase}
  .channels{position:absolute;left:73px;top:762px;display:flex;gap:6px}
  .channel{width:52px;height:52px;border-radius:50%;background:radial-gradient(circle at 40% 35%,#c81a25,#7e0a14);display:flex;align-items:center;justify-content:center}
  .clients{position:absolute;left:74px;top:858px;height:57px}
  .client{position:absolute;top:0;height:57px;background:var(--white);display:flex;align-items:center;justify-content:center;text-align:center;font-weight:600;font-size:12px;line-height:14px;color:#222}
  .client.round{border-radius:50%}
  .bottom-band{position:absolute;left:0;top:938px;width:100%;height:144px;background:var(--band)}
  .brand-dot{position:absolute;left:108px;top:21px;width:44px;height:44px;border-radius:50%;background:var(--white)}
  .brand-name{position:absolute;left:0;top:72px;width:260px;text-align:center;font-weight:700;font-size:30px;letter-spacing:1px}
  .phone{position:absolute;right:32px;top:14px;font-weight:600;font-size:46px;white-space:nowrap}
  .web{position:absolute;right:32px;top:80px;font-weight:600;font-size:25px;white-space:nowrap}
</style>
</head>
<body>
<main class="flyer">
  <header class="top-band">
    <div class="quote-frame">
      <p class="quote"><b>#1</b> SELLING TOOL TO AQUIRE NEW FRANCHISE</p>
    </div>
    <p class="quote-credit">DALE R. MARSH - CEO CASA VERDE</p>
  </header>

  <section class="dark-field" role="img" aria-label="Dark background with flowing red light-trail waves"></section>

  <div class="title-badge"><span>FRANCHISE</span></div>
  <h1 class="title-main">TESTIMONIALS</h1>
  <p class="tagline">LET YOUR FRANCHISEES DO THE SELLING...</p>

  <section class="price-panel">
    <p class="price">$10,000<small>/per Franchisee</small></p>
    <ul class="includes">
      <li>2 minute video</li>
      <li>1 minute add for your franchise's location</li>
      <li>Concept creation</li>
      <li>Communication with franchisee</li>
      <li>Travel to their location</li>
      <li>All rental equipment</li>
      <li>1 round of corrections</li>
      <li>Animated logo</li>
      <li>Licensed music</li>
    </ul>
  </section>

  <svg class="tag-string" width="838" height="1082" aria-hidden="true">
    <path d="M700 651 C 730 640, 745 700, 730 792" fill="none" stroke="#ffffff" stroke-width="2"/>
  </svg>
  <div class="discount">
    <span class="pct">25%</span>
    <span class="label">DISCOUNT</span>
    <span class="label">FOR</span>
  </div>
  <div class="tag" role="img" aria-label="Outlet Summit badge"><div class="badge"></div></div>

  <p class="section-label" style="top:733px">Use your testimonials everywhere</p>
  <div class="channels">
    <div class="channel" role="img" aria-label="Website">
      <svg width="28" height="28" viewBox="0 0 28 28" fill="none" stroke="#fff" stroke-width="1.6"><circle cx="14" cy="14" r="11"/><ellipse cx="14" cy="14" rx="5" ry="11"/><path d="M3 14h22M5 8h18M5 20h18"/></svg>
    </div>
    <div class="channel" role="img" aria-label="Video channel"></div>
    <div class="channel" role="img" aria-label="Professional network"></div>
    <div class="channel" role="img" aria-label="Social network"></div>
    <div class="channel" role="img" aria-label="Photo network"></div>
    <div class="channel" role="img" aria-label="Microblog"></div>
    <div class="channel" role="img" aria-label="Phone calls">
      <svg width="26" height="26" viewBox="0 0 24 24" fill="#fff"><path d="M6.6 10.8a15 15 0 0 0 6.6 6.6l2.2-2.2a1 1 0 0 1 1-.25 11.4 11.4 0 0 0 3.6.57 1 1 0 0 1 1 1V20a1 1 0 0 1-1 1A17 17 0 0 1 3 4a1 1 0 0 1 1-1h3.5a1 1 0 0 1 1 1c0 1.250.2 2.45.57 3.6a1 1 0 0 1-.25 1z"/></svg>
    </div>
    <div class="channel" role="img" aria-label="Emails">
      <svg width="28" height="22" viewBox="0 0 28 22" fill="none" stroke="#fff" stroke-width="2"><rect x="2" y="2" width="24" height="18" rx="2"/><path d="M2 4l12 9 12-9"/></svg>
    </div>
    <div class="channel" role="img" aria-label="In person meetings">
      <svg width="30" height="26" viewBox="0 0 30 26" fill="#fff"><circle cx="9" cy="10" r="4"/><circle cx="21" cy="10" r="4"/><path d="M2 24c0-5 3-8 7-8s7 3 7 8zM14 24c0-5 3-8 7-8s7 3 7 8z"/></svg>
    </div>
  </div>

  <p class="section-label" style="top:831px">Trusted by :</p>
  <div class="clients">
    <div class="client" style="left:0;width:120px">Rovell Auto</div>
    <div class="client round" style="left:128px;width:57px">Creamly</div>
    <div class="client" style="left:191px;width:58px">Nexa Clean</div>
    <div class="client" style="left:256px;width:77px">QuickStop</div>
    <div class="client" style="left:340px;width:85px">Tovik Smoothie</div>
  </div>

  <footer class="bottom-band">
    <div class="brand-dot"></div>
    <p class="brand-name">BRIGHTFIELD</p>
    <p class="phone">(866) 555-0172</p>
    <p class="web">www.brightfieldvoices.example</p>
  </footer>
</main>
</body>
</html>
```